Lantern Walk! A website showcasing who I am as a person

Lantern Walk started out as idea for me to better myself as a person and work on small projects that would help me grow as a person. Now I want to build a website showcasing "Lantern Walk." I want the website to showcase who I am and how I have grown both professionally and personally. I can build the raw code of the website on my own but I am not really much of a designer. I am looking for a design where I can write and post blogs, articles and share my thoughts. A little about myself and the ideas and interests that I want to share
What is Lantern Walk
Who I am
Background - Professional
Brand Marketing
Email Automation
Hiking
Rock Climbing
Traveling
Exercising and Transformation
"Personal Thoughts"
Hopefully this is enough information to get people started on some designs.
Industry/Entity Type
Work
Number of Pages Required
3 page

```html
<!DOCTYPE html>
<html lang="en">
<head>
<meta charset="utf-8">
<title>Arun Desai — Lantern Walk</title>
<link rel="stylesheet" href="https://fonts.googleapis.com/css2?family=Open+Sans:wght@400;600;700;800&display=swap">
<style>
  :root {
    --ink: #1f1f1f;
    --text: #333333;
    --muted: #6d6d6d;
    --faint: #9a9a9a;
    --line: #e6e6e6;
    --accent: #3f7fc1;
    --nav-top: #4a8cd0;
    --nav-bottom: #2f6eaf;
    --nav-active: #2a2a2a;
    --tag: #2b2b2b;
    --panel: #ffffff;
    --page: #ffffff;
    --footer: #1e1e1e;
    --fans: #3a5a99;
    --followers: #3fb0e3;
    --subscribers: #f1833a;
  }
  * { box-sizing: border-box; margin: 0; padding: 0; }
  html, body { width: 1200px; height: 2372px; overflow: hidden; background: var(--page); }
  body { font-family: "Open Sans", Arial, sans-serif; color: var(--text); }
  .canvas { position: relative; width: 1200px; height: 2372px; overflow: hidden; }

  /* Header */
  .site-header { position: absolute; left: 0; top: 0; width: 1200px; height: 87px; }
  .brand { position: absolute; left: 106px; top: 20px; font-size: 33px; font-weight: 800; letter-spacing: -0.5px; color: var(--ink); text-transform: uppercase; }
  .topics { position: absolute; left: 580px; top: 29px; font-size: 15px; color: #444; }
  .topics span.sep { margin: 0 8px; color: #999; }
  .social-mini { position: absolute; left: 986px; top: 29px; display: flex; gap: 12px; }
  .social-mini span { width: 21px; height: 21px; background: #1b1b1b; border-radius: 3px; }

  /* Navigation */
  .main-nav { position: absolute; left: 0; top: 87px; width: 1200px; height: 52px; background: linear-gradient(var(--nav-top), var(--nav-bottom)); display: flex; padding-left: 92px; }
  .main-nav a { color: #fff; text-decoration: none; font-size: 15.5px; line-height: 52px; padding: 0 14px; white-space: nowrap; }
  .main-nav a.active { background: var(--nav-active); width: 205px; text-align: center; padding: 0; margin-right: 6px; }

  /* Hero */
  .hero { position: absolute; left: 88px; top: 164px; width: 1025px; height: 514px; box-shadow: 0 2px 8px rgba(0,0,0,.25); }
  .hero-photo { position: absolute; inset: 0; background: linear-gradient(180deg, #5f95cc 0%, #a9cbe6 30%, #6c8f8a 52%, #3f6a3a 72%, #4a4a3e 100%); }
  .hero-title { position: absolute; left: 70px; top: 340px; color: #fff; font-size: 56px; font-weight: 600; letter-spacing: 1px; line-height: 1; }
  .hero-sub { position: absolute; left: 70px; top: 392px; color: #fff; font-size: 27px; font-weight: 400; }
  .hero-arrows { position: absolute; left: 68px; top: 442px; display: flex; gap: 8px; }
  .hero-arrows span { width: 26px; height: 26px; border-radius: 50%; background: rgba(0,0,0,.45); display: flex; align-items: center; justify-content: center; }

  /* Section headings & panels */
  .section-title { position: absolute; font-size: 21px; font-weight: 400; color: var(--text); text-transform: uppercase; }
  .panel { position: absolute; background: var(--panel); border-top: 2px solid var(--accent); box-shadow: 0 1px 6px rgba(0,0,0,.22); }

  /* Featured */
  .feature-card { position: absolute; width: 310px; height: 283px; overflow: hidden; }
  .feature-card .photo { position: absolute; inset: 0; }
  .feature-card .shade { position: absolute; left: 0; right: 0; bottom: 0; height: 120px; background: linear-gradient(rgba(0,0,0,0), rgba(0,0,0,.7)); }
  .feature-card h3 { position: absolute; left: 22px; bottom: 50px; color: #fff; font-size: 19px; font-weight: 400; }
  .card-meta { position: absolute; left: 22px; right: 22px; bottom: 16px; display: flex; align-items: center; color: #ddd; font-size: 11.5px; }
  .card-meta .cat { display: flex; align-items: center; gap: 10px; flex: 1; }
  .icons { display: flex; gap: 9px; }
  .icon { width: 15px; height: 15px; }
  .card-meta .icon { stroke: #eee; }

  /* Who I am */
  .avatar { position: absolute; left: 104px; top: 26px; width: 98px; height: 98px; border-radius: 50%; background: linear-gradient(#c9c4bc, #2d3340); }
  .about-name { position: absolute; top: 146px; width: 100%; text-align: center; font-size: 15px; color: #444; letter-spacing: .5px; }
  .about-text { position: absolute; left: 26px; right: 26px; top: 182px; text-align: center; font-size: 11.5px; line-height: 22px; color: var(--muted); }

  /* Popular posts */
  .post-row { position: absolute; left: 16px; width: 280px; height: 86px; border-bottom: 1px solid var(--line); }
  .post-row .thumb { position: absolute; left: 0; top: 0; width: 73px; height: 73px; }
  .post-row p, .trip-row p { position: absolute; left: 97px; top: 0; font-size: 13.5px; line-height: 21px; color: var(--text); }
  .post-row .icons, .trip-row .icons { position: absolute; left: 97px; top: 54px; }
  .post-row .icon, .trip-row .icon, .brand-date .icon { stroke: #8a8a8a; }

  /* Brand marketing */
  .brand-item { position: absolute; top: 30px; width: 198px; }
  .brand-item .thumb { width: 198px; height: 138px; }
  .brand-item p { margin-top: 16px; font-size: 13.5px; line-height: 22px; color: var(--text); }
  .brand-date { position: absolute; top: 256px; display: flex; align-items: center; gap: 10px; font-size: 12.5px; color: var(--muted); }
  .dots { position: absolute; left: 735px; top: 1468px; display: flex; gap: 6px; }
  .dots span { width: 8px; height: 8px; border-radius: 50%; background: #d0d0d0; }
  .dots span.on { background: #333; }

  /* Traveling */
  .trip-lead { position: absolute; left: 19px; top: 37px; width: 318px; height: 296px; overflow: hidden; }
  .trip-lead .photo { position: absolute; inset: 0; background: linear-gradient(160deg, #b9c4cc 0%, #c7742c 40%, #3d7fa8 62%, #34372f 100%); }
  .trip-lead .shade { position: absolute; left: 0; right: 0; bottom: 0; height: 110px; background: linear-gradient(rgba(0,0,0,0), rgba(0,0,0,.6)); }
  .trip-lead h3 { position: absolute; left: 24px; bottom: 48px; color: #fff; font-size: 18px; font-weight: 400; }
  .trip-row { position: absolute; left: 361px; width: 308px; height: 94px; border-bottom: 1px solid var(--line); }
  .trip-row .thumb { position: absolute; left: 0; top: 0; width: 79px; height: 79px; }
  .trip-row p { left: 94px; top: 4px; }
  .trip-row .icons { left: 94px; top: 56px; }

  /* Tags */
  .tags { position: absolute; left: 20px; top: 22px; width: 290px; display: flex; flex-wrap: wrap; gap: 10px 6px; }
  .tags span { background: var(--tag); color: #fff; font-size: 13px; height: 32px; line-height: 32px; padding: 0 24px; }
  .tags span.current { background: var(--accent); }

  /* Social counts */
  .count-box { position: absolute; top: 2128px; width: 98px; height: 117px; color: #fff; text-align: center; font-size: 13px; line-height: 17px; }
  .count-box .mark { width: 32px; height: 32px; border-radius: 50%; background: rgba(255,255,255,.28); margin: 18px auto 16px; }
  .fans { left: 798px; background: var(--fans); }
  .followers { left: 905px; background: var(--followers); }
  .subscribers { left: 1012px; background: var(--subscribers); }

  /* Footer */
  .site-footer { position: absolute; left: 0; top: 2281px; width: 1200px; height: 91px; background: var(--footer); color: #fff; font-size: 12.5px; }
  .footer-links { position: absolute; left: 90px; top: 36px; }
  .footer-links .sep { margin: 0 9px; }
  .copyright { position: absolute; right: 92px; top: 40px; font-size: 12px; }
</style>
</head>
<body>
<svg width="0" height="0" style="position:absolute" aria-hidden="true">
  <defs>
    <symbol id="i-user" viewBox="0 0 16 16"><circle cx="8" cy="5" r="3" fill="none" stroke-width="1.3"/><path d="M2.5 14.5c.6-3 2.8-4.5 5.5-4.5s4.9 1.5 5.5 4.5z" fill="none" stroke-width="1.3"/></symbol>
    <symbol id="i-cal" viewBox="0 0 16 16"><rect x="2" y="3" width="12" height="11" fill="none" stroke-width="1.3"/><path d="M2 6.5h12M5 1.5v3M11 1.5v3" fill="none" stroke-width="1.3"/></symbol>
    <symbol id="i-chat" viewBox="0 0 16 16"><path d="M2 2.5h12v8H7l-3 3v-3H2z" fill="none" stroke-width="1.3"/></symbol>
    <symbol id="i-folder" viewBox="0 0 16 16"><path d="M1.5 3.5h5l1.5 2h6.5v8h-13z" fill="none" stroke-width="1.3"/></symbol>
    <symbol id="i-star" viewBox="0 0 16 16"><path d="M8 1.8l1.9 4 4.3.5-3.2 2.9.9 4.3L8 11.3l-3.9 2.2.9-4.3L1.8 6.3l4.3-.5z" fill="none" stroke-width="1.3"/></symbol>
  </defs>
</svg>

<div class="canvas">
  <header class="site-header">
    <div class="brand">Arun Desai</div>
    <div class="topics">Exercising and Transformation<span class="sep">|</span>Personal Thoughts</div>
    <div class="social-mini" aria-label="Social links"><span></span><span></span><span></span><span></span></div>
  </header>

  <nav class="main-nav">
    <a class="active" href="#">WHAT IS LANTERN WALK</a>
    <a href="#">WHO I AM</a>
    <a href="#">BRAND MARKETING</a>
    <a href="#">EMAIL AUTOMATION</a>
    <a href="#">HIKING</a>
    <a href="#">ROCK CLIMBING</a>
    <a href="#">TRAVELING</a>
  </nav>

  <section class="hero">
    <div class="hero-photo" role="img" aria-label="Two hikers celebrating on a rocky summit above a green coastal valley under a blue sky"></div>
    <h1 class="hero-title">LANTERN WALK.</h1>
    <p class="hero-sub">Neque porro quisquam est</p>
    <div class="hero-arrows">
      <span><svg width="10" height="10" viewBox="0 0 10 10"><path d="M6.5 1.5L3 5l3.5 3.5" stroke="#fff" stroke-width="1.6" fill="none"/></svg></span>
      <span><svg width="10" height="10" viewBox="0 0 10 10"><path d="M3.5 1.5L7 5 3.5 8.5" stroke="#fff" stroke-width="1.6" fill="none"/></svg></span>
    </div>
  </section>

  <!-- Featured articles -->
  <h2 class="section-title" style="left:96px;top:730px;">Featured Articles</h2>
  <section class="panel" style="left:93px;top:768px;width:690px;height:639px;">
    <article class="feature-card" style="left:24px;top:24px;">
      <div class="photo" role="img" aria-label="Smiling businessman in a suit holding a tablet in an office" style="background:linear-gradient(135deg,#6f7d86,#3a4650 60%,#20262c);"></div>
      <div class="shade"></div>
      <h3>Neque porro quisquam est</h3>
      <div class="card-meta"><span class="cat"><svg class="icon"><use href="#i-folder"/></svg>News</span><span class="icons"><svg class="icon"><use href="#i-user"/></svg><svg class="icon"><use href="#i-cal"/></svg><svg class="icon"><use href="#i-chat"/></svg></span></div>
    </article>
    <article class="feature-card" style="left:358px;top:24px;">
      <div class="photo" role="img" aria-label="Bearded man with glasses working at a laptop by a bookshelf" style="background:linear-gradient(135deg,#b7a892,#6b5a48 55%,#2c2a2a);"></div>
      <div class="shade"></div>
      <h3>Neque porro quisquam est</h3>
      <div class="card-meta"><span class="cat"><svg class="icon"><use href="#i-folder"/></svg>Business , Seo</span><span class="icons"><svg class="icon"><use href="#i-user"/></svg><svg class="icon"><use href="#i-cal"/></svg><svg class="icon"><use href="#i-chat"/></svg></span></div>
    </article>
    <article class="feature-card" style="left:24px;top:330px;">
      <div class="photo" role="img" aria-label="Tourist couple in hats reading a map in front of an old building" style="background:linear-gradient(135deg,#e0c9a8,#b07a5a 55%,#4b3d34);"></div>
      <div class="shade"></div>
      <h3>Neque porro quisquam est</h3>
      <div class="card-meta"><span class="cat"><svg class="icon"><use href="#i-folder"/></svg>Business</span><span class="icons"><svg class="icon"><use href="#i-user"/></svg><svg class="icon"><use href="#i-cal"/></svg></span></div>
    </article>
    <article class="feature-card" style="left:358px;top:330px;">
      <div class="photo" role="img" aria-label="Backpacker looking at snowy mountain peaks" style="background:linear-gradient(180deg,#4b86c6,#a9c2dc 45%,#5b5a58 75%,#2c2b2a);"></div>
      <div class="shade"></div>
      <h3>Neque porro quisquam est</h3>
      <div class="card-meta"><span class="cat"><svg class="icon"><use href="#i-folder"/></svg>Tech</span><span class="icons"><svg class="icon"><use href="#i-user"/></svg><svg class="icon"><use href="#i-cal"/></svg><svg class="icon"><use href="#i-chat"/></svg></span></div>
    </article>
  </section>

  <!-- Who I am -->
  <h2 class="section-title" style="left:799px;top:730px;">Who I Am</h2>
  <section class="panel" style="left:795px;top:768px;width:316px;height:332px;">
    <div class="avatar" role="img" aria-label="Portrait of the author in a suit"></div>
    <div class="about-name">DOLOREM IPSUM</div>
    <p class="about-text">It is a long established fact that a reader will be distracted by the readable content of a page when looking at its layout. The point of using Lorem Ipsum is that it has a more-or-less normal distribution of letters, as opposed</p>
  </section>

  <!-- Popular posts -->
  <h2 class="section-title" style="left:799px;top:1128px;">Popular Posts</h2>
  <section class="panel" style="left:795px;top:1166px;width:316px;height:636px;">
    <div class="post-row" style="top:22px;"><div class="thumb" role="img" aria-label="Woman walking through a field" style="background:linear-gradient(135deg,#c9a27a,#7d5a3c);"></div><p>Ipsum is simply dummy text<br>of the printing and type</p><span class="icons"><svg class="icon"><use href="#i-star"/></svg><svg class="icon"><use href="#i-cal"/></svg><svg class="icon"><use href="#i-user"/></svg></span></div>
    <div class="post-row" style="top:117px;"><div class="thumb" role="img" aria-label="Laptop and notes on a desk" style="background:linear-gradient(135deg,#6e8fb2,#2f3c4f);"></div><p>Ipsum is simply dummy text<br>of the printing and type</p><span class="icons"><svg class="icon"><use href="#i-cal"/></svg><svg class="icon"><use href="#i-user"/></svg><svg class="icon"><use href="#i-chat"/></svg></span></div>
    <div class="post-row" style="top:212px;"><div class="thumb" role="img" aria-label="Travelling couple outdoors" style="background:linear-gradient(135deg,#c8b29a,#8a5b45);"></div><p>Ipsum is simply dummy text<br>of the printing and type</p><span class="icons"><svg class="icon"><use href="#i-star"/></svg><svg class="icon"><use href="#i-cal"/></svg><svg class="icon"><use href="#i-user"/></svg><svg class="icon"><use href="#i-chat"/></svg></span></div>
    <div class="post-row" style="top:307px;"><div class="thumb" role="img" aria-label="Businessman crouching on a white background" style="background:linear-gradient(135deg,#e8e8e8,#3d4658);"></div><p>Ipsum is simply dummy text<br>of the printing and type</p><span class="icons"><svg class="icon"><use href="#i-cal"/></svg><svg class="icon"><use href="#i-user"/></svg><svg class="icon"><use href="#i-chat"/></svg></span></div>
    <div class="post-row" style="top:402px;"><div class="thumb" role="img" aria-label="Traveller reading a map at dusk" style="background:linear-gradient(135deg,#d59a4e,#3b2c26);"></div><p>Ipsum is simply dummy text<br>of the printing and type</p><span class="icons"><svg class="icon"><use href="#i-cal"/></svg><svg class="icon"><use href="#i-user"/></svg><svg class="icon"><use href="#i-chat"/></svg></span></div>
    <div class="post-row" style="top:497px;"><div class="thumb" role="img" aria-label="Hiker with a backpack on a trail" style="background:linear-gradient(135deg,#b89a6a,#5a4630);"></div><p>Ipsum is simply dummy text<br>of the printing and type</p><span class="icons"><svg class="icon"><use href="#i-cal"/></svg><svg class="icon"><use href="#i-user"/></svg><svg class="icon"><use href="#i-chat"/></svg></span></div>
  </section>

  <!-- Brand marketing -->
  <h2 class="section-title" style="left:90px;top:1458px;">Brand Marketing</h2>
  <div class="dots"><span></span><span class="on"></span><span></span></div>
  <section class="panel" style="left:90px;top:1496px;width:693px;height:306px;">
    <div class="brand-item" style="left:24px;"><div class="thumb" role="img" aria-label="Presenter in front of a whiteboard covered in branding sketches" style="background:linear-gradient(135deg,#e9e4dc,#9aa3b0 60%,#5a4a44);"></div><p>Ipsum is simply dummy text<br>of the printing and type</p></div>
    <div class="brand-date" style="left:24px;"><svg class="icon"><use href="#i-cal"/></svg>27 March, 2017</div>
    <div class="brand-item" style="left:243px;"><div class="thumb" role="img" aria-label="Team collaborating around a table with laptops" style="background:linear-gradient(135deg,#e5c4c0,#b88a8a 55%,#6e6a72);"></div><p>Ipsum is simply dummy text<br>of the printing and type</p></div>
    <div class="brand-date" style="left:243px;"><svg class="icon"><use href="#i-cal"/></svg>7 March, 2017</div>
    <div class="brand-item" style="left:464px;"><div class="thumb" role="img" aria-label="Wooden desk with notebook, glasses and coffee cup" style="background:linear-gradient(135deg,#9c7a55,#c8a779 50%,#5e4630);"></div><p>Ipsum is simply dummy text<br>of the printing and type</p></div>
    <div class="brand-date" style="left:464px;"><svg class="icon"><use href="#i-cal"/></svg>1 January, 2017</div>
  </section>

  <!-- Traveling -->
  <h2 class="section-title" style="left:88px;top:1830px;">Traveling</h2>
  <section class="panel" style="left:90px;top:1867px;width:693px;height:376px;">
    <article class="trip-lead">
      <div class="photo" role="img" aria-label="Couple hiking with poles through autumn forest"></div>
      <div class="shade"></div>
      <h3>Porro quisquam est</h3>
      <div class="card-meta"><span class="cat"><svg class="icon"><use href="#i-folder"/></svg>Interview</span><span class="icons"><svg class="icon"><use href="#i-user"/></svg><svg class="icon"><use href="#i-cal"/></svg><svg class="icon"><use href="#i-chat"/></svg></span></div>
    </article>
    <div class="trip-row" style="top:41px;"><div class="thumb" role="img" aria-label="Person leaping on a beach at sunset" style="background:linear-gradient(180deg,#c9d3dc,#d9a36a);"></div><p>Ipsum is simply dummy text<br>of the printing and type</p><span class="icons"><svg class="icon"><use href="#i-star"/></svg><svg class="icon"><use href="#i-cal"/></svg><svg class="icon"><use href="#i-user"/></svg></span></div>
    <div class="trip-row" style="top:144px;"><div class="thumb" role="img" aria-label="Airplane flying in a blue sky" style="background:linear-gradient(180deg,#3d7fc0,#bfd6ea);"></div><p>Ipsum is simply dummy text<br>of the printing and type</p><span class="icons"><svg class="icon"><use href="#i-cal"/></svg><svg class="icon"><use href="#i-user"/></svg><svg class="icon"><use href="#i-chat"/></svg></span></div>
    <div class="trip-row" style="top:247px;"><div class="thumb" role="img" aria-label="Travel essentials laid out flat with sunglasses" style="background:linear-gradient(135deg,#7fbcd0,#2e3b44 55%,#d7b67c);"></div><p>Ipsum is simply dummy text<br>of the printing and type</p><span class="icons"><svg class="icon"><use href="#i-star"/></svg><svg class="icon"><use href="#i-cal"/></svg><svg class="icon"><use href="#i-user"/></svg><svg class="icon"><use href="#i-chat"/></svg></span></div>
  </section>

  <!-- Tags -->
  <h2 class="section-title" style="left:801px;top:1830px;">Tags</h2>
  <section class="panel" style="left:798px;top:1867px;width:313px;height:247px;">
    <div class="tags">
      <span>News</span><span>business</span>
      <span>Hiking</span><span>Email Automation</span>
      <span>Travel</span><span>Rock Climbing</span>
      <span class="current">Who I am</span><span>What is Lantern Walk</span>
      <span>Brand Marketing</span>
    </div>
  </section>

  <div class="count-box fans"><div class="mark"></div>259<br>fans</div>
  <div class="count-box followers"><div class="mark"></div>568<br>followers</div>
  <div class="count-box subscribers"><div class="mark"></div>101<br>subscribers</div>

  <footer class="site-footer">
    <div class="footer-links">ABOUT<span class="sep">|</span>PRIVACY<span class="sep">|</span>TERMS<span class="sep">|</span>LEGAL<span class="sep">|</span>CONTACT</div>
    <div class="copyright">Copyright © 2017 &nbsp;All Rights Reserved</div>
  </footer>
</div>
</body>
</html>
```